Law Office needs stationery design and business card

I currently have been using the same letterhead for the last 8 years. Since i 'm about to adding another location, I want to revamp my letterhead and business card. I already have a logo i'm happy with. I will upload my current letterhead, fax sheet, envelope, and logos. I need a business card also. I have 2 locations, 1 phone number, 1 fax line, website, etc. If possible and fitting with the design, I would like to keep the same information listed currently on the letterhead.

**Keep in mind, I also NEED A FAX SHEET COVER. thank you

Hello, Please submit a Gray Scale or Black and White version of your designs also, since most of the time I will be printing NON color stationery. I will seldom use a color print for my letterhead, I would like to have a color version for my benefit, however i will print in grayscale majority of the time . For the Business Card, that can just be in color. When I get my business cards they will be in color.Thank youEnrique Added Sunday, September 18, 2016

```html
<!DOCTYPE html>
<html lang="en">
<head>
<meta charset="utf-8">
<title>Marvell Law – Business Card</title>
<link rel="stylesheet" href="https://fonts.googleapis.com/css2?family=Libre+Baskerville&family=Open+Sans:ital,wght@0,400;1,700&display=swap">
<style>
  :root {
    --backdrop: #d2c27e;
    --cream: #fbf7ea;
    --cream-edge: #f1e6c6;
    --paper: #ffffff;
    --gold: #b08d3e;
    --gold-deep: #9c7a2f;
    --ink: #1c1a17;
    --band-text: #ffffff;
    --mark-faint: #e4e2dc;
  }
  * { margin: 0; padding: 0; box-sizing: border-box; }
  html, body { width: 1200px; height: 801px; overflow: hidden; }
  body {
    background: var(--backdrop);
    font-family: "Open Sans", Arial, sans-serif;
    position: relative;
  }
  .card {
    position: absolute;
    top: 257px;
    width: 500px;
    height: 286px;
    box-shadow: 0 10px 24px rgba(60, 50, 20, 0.25);
    overflow: hidden;
  }
  .card--front { left: 65px; background: var(--cream); }
  .card--back { left: 635px; background: var(--paper); }

  .card--front .card__edge {
    position: absolute; left: 0; right: 0; bottom: 0; height: 22px;
    background: linear-gradient(var(--cream), var(--cream-edge));
  }

  .wordmark {
    display: flex; align-items: center; gap: 12px;
  }
  .wordmark__square {
    width: 34px; height: 34px; background: var(--ink);
    transform: rotate(-8deg);
  }
  .wordmark__name {
    font-family: "Libre Baskerville", Georgia, serif;
    color: var(--gold-deep);
    font-size: 26px;
    letter-spacing: 0.5px;
    white-space: nowrap;
  }
  .attorney {
    font-family: "Open Sans", Arial, sans-serif;
    font-style: italic; font-weight: 700;
    color: var(--gold);
    font-size: 15px;
  }

  .card--front .brand {
    position: absolute; left: 0; right: 0; top: 98px;
    display: flex; flex-direction: column; align-items: center; gap: 8px;
  }

  .card--back .brand {
    position: absolute; left: 30px; top: 96px;
    display: flex; flex-direction: column; gap: 6px;
  }
  .card--back .wordmark__name { font-size: 22px; }
  .card--back .wordmark__square { width: 28px; height: 28px; }
  .card--back .attorney { font-size: 13px; padding-left: 40px; }

  .faint-square {
    position: absolute; right: 70px; top: 22px;
    width: 78px; height: 78px; background: var(--mark-faint);
    transform: rotate(-8deg);
  }

  .contact-band {
    position: absolute; left: 0; right: 0; bottom: 0; height: 62px;
    background: var(--gold);
    color: var(--band-text);
    font-size: 10.5px;
    display: flex; justify-content: space-between;
    padding: 10px 18px;
  }
  .contact-band ul { list-style: none; display: flex; flex-direction: column; gap: 5px; }
  .contact-band li { display: flex; align-items: center; gap: 6px; white-space: nowrap; }
  .contact-band .row { display: flex; gap: 12px; }
  .contact-band svg { width: 11px; height: 11px; flex: none; }
</style>
</head>
<body>

  <section class="card card--front" aria-label="Business card front">
    <div class="brand">
      <div class="wordmark">
        <span class="wordmark__square"></span>
        <span class="wordmark__name">MARVELL LAW</span>
      </div>
      <p class="attorney">Gustavo Marvell Esq.</p>
    </div>
    <div class="card__edge"></div>
  </section>

  <section class="card card--back" aria-label="Business card back">
    <div class="faint-square"></div>
    <div class="brand">
      <div class="wordmark">
        <span class="wordmark__square"></span>
        <span class="wordmark__name">MARVELL LAW</span>
      </div>
      <p class="attorney">Gustavo Marvell Esq.</p>
    </div>

    <div class="contact-band">
      <ul class="addresses">
        <li>
          <svg viewBox="0 0 12 12"><circle cx="6" cy="6" r="5.5" fill="#fff"/><path d="M6 2.5a2.2 2.2 0 0 0-2.2 2.2C3.8 6.4 6 9.3 6 9.3s2.2-2.9 2.2-4.6A2.2 2.2 0 0 0 6 2.5z" fill="var(--gold)"/></svg>
          418 North Elm St., Suite 200, Lindale, PA 19220
        </li>
        <li>
          <svg viewBox="0 0 12 12"><circle cx="6" cy="6" r="5.5" fill="#fff"/><path d="M6 2.5a2.2 2.2 0 0 0-2.2 2.2C3.8 6.4 6 9.3 6 9.3s2.2-2.9 2.2-4.6A2.2 2.2 0 0 0 6 2.5z" fill="var(--gold)"/></svg>
          76 Harbor Ave, Westbrook, PA 19310
        </li>
      </ul>
      <ul class="lines">
        <li class="row">
          <span style="display:flex;align-items:center;gap:6px">
            <svg viewBox="0 0 12 12"><circle cx="6" cy="6" r="5.5" fill="#fff"/><path d="M4 3l1.2 1.4-.6.9c.4.9 1 1.5 1.9 1.9l.9-.6L9 7.8 8.3 9C6 9 3 6 3 3.7z" fill="var(--gold)"/></svg>
            610.555.0182
          </span>
          <span style="display:flex;align-items:center;gap:6px">
            <svg viewBox="0 0 12 12"><circle cx="6" cy="6" r="5.5" fill="#fff"/><rect x="3" y="5" width="6" height="3.5" fill="var(--gold)"/><rect x="4" y="3" width="4" height="2" fill="var(--gold)"/></svg>
            484.555.0147
          </span>
        </li>
        <li class="row">
          <span style="display:flex;align-items:center;gap:6px">
            <svg viewBox="0 0 12 12"><circle cx="6" cy="6" r="5.5" fill="#fff"/><circle cx="6" cy="6" r="3.2" fill="none" stroke="var(--gold)" stroke-width="1"/><path d="M2.8 6h6.4M6 2.8c-1.6 2-1.6 4.4 0 6.4M6 2.8c1.6 2 1.6 4.4 0 6.4" fill="none" stroke="var(--gold)" stroke-width=".8"/></svg>
            www.MarvellLaw.com
          </span>
          <span style="display:flex;align-items:center;gap:6px">
            <svg viewBox="0 0 12 12"><circle cx="6" cy="6" r="5.5" fill="#fff"/></svg>
            MarvellLaw
          </span>
        </li>
      </ul>
    </div>
  </section>

</body>
</html>
```